KMT Packaging design for beauty industry

Looking for my first product packaging design, tailored to reflect KMT’s branding and product benefits, along with mockup suggestions to bring it to life.

---

Front of the Box Copy
**Header**:
KMT Ionic Elite Stand-Up Dryer

**Subheader**:
Effortless Styling. Professional Results.

**Features (Use Icons + Text)**:
- **Adjustable Height**: Perfect for all users and settings.
- **Ionic Technology**: Faster drying, frizz-free results.
- **360° Heat Distribution**: Even styling every time.
- **Lightweight & Portable**: Easy to move and assemble.

**Call to Action (CTA)**:
*“Elevate Your Look with KMT Professional-Grade Tools.”*

---

### **Side Panel Copy**
**About KMT**:
"At KMT, we believe beauty is power. Our tools are designed with precision, ensuring every style feels as beautiful as you are."

**Key Benefits**:
- 3 Heat Settings for customizable control.
- Quiet operation for a professional salon experience.
- Compact foldable design for storage and travel.

**Contact Info**:
KMT Beauty | **www.KMTglowline.com**
Customer Care: care@KMTglowline.com

---

### **Back Panel Copy**
**Product Specifications**:
- Voltage: 110V-240V
- Adjustable Height Range: X to Y inches
- Dryer Weight: X lbs

**What’s Included**:
- 1 Stand-Up Dryer
- Adjustable Stand
- User Manual

**Care Instructions**:
"Clean with a damp cloth after use. Store in a cool, dry place."

**Certifications**:
(Include icons for QX, CE, RoHS, and recycling).

**Barcode Area**: Leave space for the UPC code.

---

### **Mockup Suggestions**
1. **Front View**:
- Use a glossy royal purple background with a clean, central placement of the KMT logo in metallic gold.
- Include a product photo or 3D render in high resolution showing the dryer in action or as a standalone image.
- Highlight features using icons with gold or white text.

2. **Side View**:
- Use a lifestyle image (e.g., a stylist using the dryer in a salon).
- Incorporate a vertical gold stripe or gradient to add luxury while separating text sections.

3. **Back View**:
- A clean layout with product details, specifications, and what's included.
- Use gold accents to frame sections for easy readability.

4. **Top Panel**:
- Simple branding with just the KMT logo and tagline: *"Keep Making Trends."*

The competition:
https://www.velmorashop.com/products/swift-blaze-07142?ref=QzT4pLm8Wn2Rv6Xc

Feel free to use the phots by the "the completion" but remove logo and add KMT logo .
https://files.pondercloud.com/folders/7gRt2KqWz9LmXv4NbPa?share=link
Size: 48x36.5x48 CM

Logo: https://files.pondercloud.com/folders/7gRt2KqWz9LmXv4NbPa?share=link
Also im not able to attached the AI file of the logo. Please message me your email and I'll email it to you.

Thank you!
Happy designing!

Target Market(s)

Target Audience for KMT’s First Product Demographics: Age: 18-40 years old Gender: Primarily women Income Level: Middle to upper-middle income, willing to invest in quality beauty products. Geographics: Urban and suburban areas across the U.S., where beauty culture is strong and highly influenced by social media and fashion trends. Psychographics: Beauty Enthusiasts: Individuals who prioritize their appearance and enjoy experimenting with beauty products. Trendsetters: Consumers who follow the latest beauty trends, influenced by social media and influencers. Self-Expression Advocates: Those who see beauty as a form of self-care and a way to express their personality and confidence. Behavioral Characteristics: Purchase Habits: Frequently buy beauty tools and products online or in beauty supply stores. Look for high-quality, professional-grade, and aesthetically pleasing products. Product Expectations: Easy-to-use, reliable, and results-driven. Luxurious feel without an excessively high price point. Engagement: Active on social media platforms like Pictavia, ZapReel, and ViewLoom. Trust peer reviews, influencer recommendations, and user-generated content. Customer Needs: Products that simplify beauty routines. Tools and supplies that are versatile and cater to diverse beauty needs, particularly for African American women (a key segment for KMT).

Industry/Entity Type

Industry Overview Primary Industry: Beauty and Personal Care: Encompasses products and tools for hair, skin, nails, and cosmetics. Sub-Sector: Hair Care & Styling Tools: Includes professional-grade tools like dryers, flat irons, and curling wands, along with supporting products like shampoos, conditioners, and styling creams.

Font styles to use
Serif

Requirements
Must have
• Must-Haves for the Packaging Brand Identity: Prominent display of the KMT logo in metallic gold to reinforce brand recognition. Consistent use of royal purple as the background color with metallic gold and white typography for a luxurious feel. Clear Product Information: Product Name: Clearly labeled as "KMT Ionic Elite Stand-Up Dryer" on the front. Key Features: Use icons with text to highlight: Adjustable Height Ionic Technology 360° Heat Distribution Lightweight & Portable Visual Appeal: High-quality product image or 3D render showcasing the dryer. Lifestyle imagery on the side panels to show the product in use, emphasizing its professional and stylish appeal. Call to Action (CTA): Include a tagline like: “Elevate Your Look with KMT Professional-Grade Tools.” Functional Details: Product Specifications: Include voltage, dimensions, and weight on the back panel. What’s Included: Clearly list all box contents. Certifications and Compliance: Add icons for QX, CE, RoHS, and recycling to ensure credibility and eco-conscious appeal. Contact Information: Website: www.KMTglowline.com Customer care email: care@KMTglowline.com Barcode Area: Leave space for the UPC code on the back panel. Packaging Consistency: Uniform design elements across all panels for a cohesive look (color scheme, typography, and layout). Professional and Luxurious Finish: A glossy or matte finish with possible embossing on the logo for a premium touch.
Nice to have
• Nice-to-Have Elements Interactive Design Features: QR Code: Link to a demo video, tutorial, or assembly instructions for added customer engagement. Augmented Reality (AR): An AR feature that allows customers to see the dryer in a 360° view or visualize it in their space. Texture and Finishes: Embossed or Debossed Details: Highlight the KMT logo or key features with embossed or debossed effects for a tactile, premium feel. Spot UV Coating: Add gloss to key areas like the logo or icons to make them pop. Eco-Friendly Touch: Recyclable or biodegradable materials for the packaging. A small section emphasizing sustainability with a message like: “KMT is committed to beauty and the environment.” Unique Structural Design: Magnetic flap or window cutout to allow customers to peek at the product inside. A handle or carrying feature for easy transport, aligning with the portable nature of the dryer. Inspirational Touch: Include a short, empowering quote or message on the inside flap, such as: “Every style tells a story—KMT helps you write yours.” Custom Illustrations: Subtle, artistic illustrations (e.g., flowing hair, heat waves) integrated into the design background to emphasize beauty and technology. Additional Branding Elements: A tagline or hashtag like #KMTRadiance to encourage customers to share their experience on social media. Icons or badges for unique selling points, such as "Professional-Grade Quality" or "Salon Approved." Convenience Features: Printed assembly instructions or key features inside the box for ease of use. Perforated areas for easy opening. Color Gradients or Patterns: Add subtle gradients in the royal purple background for depth. Incorporate gold patterns (like geometric shapes or soft waves) for a modern touch. Seasonal or Limited-Edition Elements: A special ribbon or sticker indicating a “First Edition” or “Limited Release” to create exclusivity.
Should not have
• What the Packaging Should NOT Have Overcrowded Design: Avoid cluttering the box with too much text, small icons, or excessive design elements. A clean and elegant layout is key. Low-Quality Imagery: Do not use low-resolution product photos or stock images that don’t align with the premium look of your brand. Overused or Generic Icons: Skip overly common or generic symbols (e.g., basic checkmarks or lightning bolts). Custom, elegant icons are more appealing. Inconsistent Branding: Do not use colors, fonts, or design elements that stray from the royal purple, gold, and white branding. Consistency builds recognition. Unclear Information: Avoid vague or ambiguous descriptions. Clearly explain features, benefits, and product specifications. Cheap Materials: Packaging that feels flimsy or poorly constructed can reduce perceived value. Invest in durable materials. Overly Trendy Fonts: Avoid overly decorative or hard-to-read fonts. Stick with modern, clean typography that aligns with luxury branding. Busy Backgrounds: Don’t use loud patterns, excessive gradients, or background images that distract from key elements like the logo and product image. Misleading Claims: Avoid exaggerated or false claims (e.g., “World’s Best Dryer”) that could harm your brand’s credibility. Unnecessary Jargon: Avoid overly technical language that might confuse customers. Use simple, benefit-driven terms instead. Cliché Beauty Imagery: Skip generic, overused beauty symbols (e.g., oversized hair strands or glowing light effects) that don’t add value or originality. Lack of Contrast: Ensure text is easily readable. Avoid color combinations (like gold on light backgrounds) that reduce legibility. Lack of Accessibility: Don’t forget about inclusive design. Avoid small text or icons that are hard to read for visually impaired customers.

```html
<!DOCTYPE html>
<html lang="en">
<head>
<meta charset="utf-8">
<title>KMT Ionic Elite Stand-Up Dryer — Side Panel</title>
<link rel="stylesheet" href="https://fonts.googleapis.com/css2?family=Cormorant+Garamond:wght@500&family=Noto+Serif:ital,wght@0,400;1,400;1,600&display=swap">
<style>
  :root {
    --royal-purple: #561b6b;
    --royal-purple-light: #5f2d72;
    --gold: #c9a24a;
    --gold-light: #e6c877;
    --white: #f7f2f8;
    --backdrop: #ffffff;
    --icon-dark: #2b2630;
    --photo-dark: #3a3a3a;
    --photo-light: #b9b9b9;
  }
  * { box-sizing: border-box; margin: 0; padding: 0; }
  html, body {
    width: 1200px; height: 900px; overflow: hidden;
    background: var(--backdrop);
  }
  .side-panel {
    position: absolute; left: 270px; top: 20px;
    width: 660px; height: 860px;
    background: linear-gradient(135deg, var(--royal-purple) 0%, var(--royal-purple) 55%, var(--royal-purple-light) 100%);
    color: var(--white);
  }
  .panel-heading {
    position: absolute; top: 64px; left: 0; right: 0;
    text-align: center;
    font-family: "Cormorant Garamond", serif;
    font-weight: 500; font-size: 62px; letter-spacing: -1px;
    color: var(--gold);
  }
  .brand-quote {
    position: absolute; top: 150px; left: 110px; right: 110px;
    text-align: center;
    font-family: "Noto Serif", serif; font-style: italic;
    font-size: 15.5px; line-height: 1.3;
  }
  .lifestyle-photo {
    position: absolute; top: 222px; left: 172px;
    width: 320px; height: 320px; border-radius: 50%;
    border: 3px solid var(--gold);
    background: radial-gradient(circle at 45% 40%, var(--photo-light) 0%, #8a8a8a 45%, var(--photo-dark) 100%);
  }
  .benefits {
    position: absolute; top: 600px; left: 164px;
    width: 336px; height: 150px;
    border: 1.5px solid var(--gold);
    display: flex;
  }
  .benefit {
    flex: 1; display: flex; flex-direction: column; align-items: center;
    padding-top: 14px;
  }
  .benefit + .benefit { border-left: 1.5px solid var(--gold); }
  .benefit-icon { width: 68px; height: 68px; }
  .benefit-text {
    margin-top: 8px; padding: 0 6px; text-align: center;
    font-family: "Noto Serif", serif; font-style: italic; font-weight: 600;
    font-size: 11px; line-height: 1.2;
  }
  .contact {
    position: absolute; left: 86px; bottom: 40px;
    font-family: "Noto Serif", serif; font-size: 11px; line-height: 2;
  }
</style>
</head>
<body>
  <section class="side-panel">
    <h1 class="panel-heading">About KMT</h1>
    <p class="brand-quote">"At KMT, we believe beauty is power. Our tools are designed with precision, ensuring every style feels as beautiful as you are."</p>
    <div class="lifestyle-photo" role="img" aria-label="Black and white lifestyle photo of a smiling woman seated under a hooded stand-up dryer in a salon"></div>

    <div class="benefits">
      <div class="benefit">
        <svg class="benefit-icon" viewBox="0 0 68 68" aria-hidden="true">
          <circle cx="34" cy="34" r="32" fill="var(--icon-dark)" stroke="var(--gold)" stroke-width="1.5"/>
          <circle cx="36" cy="34" r="15" fill="none" stroke="var(--white)" stroke-width="1.5"/>
          <line x1="36" y1="34" x2="44" y2="24" stroke="var(--white)" stroke-width="1.5"/>
          <circle cx="18" cy="28" r="1.3" fill="var(--white)"/>
          <circle cx="17" cy="34" r="1.3" fill="var(--white)"/>
          <circle cx="18" cy="40" r="1.3" fill="var(--white)"/>
        </svg>
        <p class="benefit-text">3 Heat Settings for customizable control.</p>
      </div>
      <div class="benefit">
        <svg class="benefit-icon" viewBox="0 0 68 68" aria-hidden="true">
          <circle cx="34" cy="34" r="32" fill="var(--icon-dark)" stroke="var(--gold)" stroke-width="1.5"/>
          <path d="M22 28 h7 l9 -8 v28 l-9 -8 h-7 z" fill="none" stroke="var(--white)" stroke-width="1.5" stroke-linejoin="round"/>
          <path d="M42 28 q4 6 0 12" fill="none" stroke="var(--white)" stroke-width="1.5"/>
          <line x1="20" y1="20" x2="48" y2="48" stroke="var(--white)" stroke-width="1.5"/>
        </svg>
        <p class="benefit-text">Quiet operation for a professional salon experience.</p>
      </div>
      <div class="benefit">
        <svg class="benefit-icon" viewBox="0 0 68 68" aria-hidden="true">
          <circle cx="34" cy="34" r="32" fill="var(--icon-dark)" stroke="var(--gold)" stroke-width="1.5"/>
          <rect x="28" y="18" width="12" height="12" fill="var(--white)"/>
          <path d="M18 40 h10 l6 3 h10 l6 -4 v4 l-8 6 h-14 l-10 -3 z" fill="var(--white)"/>
        </svg>
        <p class="benefit-text">Compact foldable design for storage and travel.</p>
      </div>
    </div>

    <address class="contact" style="font-style:normal">
      KMT Beauty | www.KMTglowline.com<br>
      Customer Care: care@KMTglowline.com
    </address>
  </section>
</body>
</html>
```